TLV8 Print + Graphic Design

We have already used pixel fair for our logo design, which has come out really well. Right now we also running a design contest for our business card, please feel free to participate (contest name: TLV8 Business Card Design Project).
We have our logo design completed and we want the creative designers to now come out with all the other designs for TLV8 needs,
1. Brochure design based on the logo colours (4-8 pages)
2. Tri fold flyer designs based on the logo colours
3. Powerpoint templates for our presentations
4. Letter head designs (A4 & A3)
5. Tech Cases (http://www.brenvale.com.au/webapp/wcs/stores/servlet/ProductDisplay?storeId=47120&langId=10&catalogId=31008&categoryId=512937&productId=40817264&imagePath=QTR0047305)
There should be synergy and continuance across all designs, we use a lot of power-point presentations and continued changes to brochures, so we need these to stand out in graphic design with elegance and class.
Powerpoint / Brochure / Flyer should have the following,
1. Place for photos, charts, texts and sections.
2. Final page to contain our contact details (social + mobile + address)
3. Templates editable by word or powerpoint or illustrator
Thank you and all the best.
For details about the company please visit, www.tlv8.com.
Target Market(s)
visit www.tlv8.com
Industry/Entity Type
Graphic Design

```html
<!DOCTYPE html>
<html lang="en">
<head>
<meta charset="utf-8">
<title>TLV8 Brochure Pages</title>
<link rel="stylesheet" href="https://fonts.googleapis.com/css2?family=Gelasio:ital@1&family=Open+Sans:wght@300;400&display=swap">
<style>
  :root {
    --board: #2b302f;
    --paper: #ffffff;
    --accent-gold: #b5c94a;
    --brand-green: #45b37f;
    --leaf-green: #9dc33c;
    --deep-green: #3aaa55;
    --soft-green: #a4cc6a;
    --body-grey: #6a6a6a;
    --orange-stone: #c7701c;
    --white-stone: #ececec;
    --grey-vein: #b9b9b9;
    --beige-stone: #d9bfa4;
    --green-stone: #3a9a5c;
    --blue-stone: #3f6a98;
  }
  * { margin: 0; padding: 0; box-sizing: border-box; }
  html, body { width: 1200px; height: 748px; overflow: hidden; background: var(--board); }
  .board { position: relative; width: 1200px; height: 748px; font-family: "Open Sans", Arial, sans-serif; }
  .board-title {
    position: absolute; top: 30px; left: 0; width: 1200px; text-align: center;
    font-family: "Gelasio", Georgia, serif; font-style: italic; font-weight: 400;
    font-size: 25px; color: var(--accent-gold);
  }
  .page { position: absolute; top: 93px; width: 419px; height: 606px; background: var(--paper); overflow: hidden; }
  .page--one { left: 99px; }
  .page--two { left: 652px; }
  .caption {
    position: absolute; top: 712px; width: 419px; text-align: center;
    font-family: "Gelasio", Georgia, serif; font-style: italic; font-size: 15px; color: var(--accent-gold);
  }
  .caption--one { left: 99px; }
  .caption--two { left: 612px; }
  .block { position: absolute; }

  .wordmark { position: absolute; top: 18px; display: flex; align-items: center; gap: 6px;
    font-size: 20px; font-weight: 400; color: var(--brand-green); letter-spacing: 0.5px; }
  .wordmark-dot { width: 12px; height: 12px; border-radius: 50%; background: var(--leaf-green); }

  .section-tab { background: var(--brand-green); color: #fff; }
  .page--one .section-tab { left: 25px; top: 0; width: 212px; height: 66px; }
  .section-tab-title { position: absolute; left: 30px; top: 20px; font-size: 25px; font-weight: 400; }

  .product-title { left: 55px; top: 156px; font-size: 26px; font-weight: 300; color: var(--brand-green); }
  .product-copy { left: 52px; top: 216px; width: 166px; font-size: 7.6px; line-height: 12.2px; color: var(--body-grey); }
  .product-copy p { margin-bottom: 12px; }

  .photo-lobby { left: 238px; top: 158px; width: 167px; height: 124px;
    background: linear-gradient(160deg, #e8dcb8 0%, #b99a55 35%, #6f7a3e 55%, #d8cdb0 80%, #efe8d8 100%); }

  .tile { position: absolute; }
  .tile--orange { background: radial-gradient(circle at 40% 40%, #e08a2a, var(--orange-stone) 60%, #9c5412); }
  .tile--grey-vein { background: linear-gradient(135deg, #f4f4f4, var(--grey-vein) 45%, #f2f2f2 60%, #9a9a9a 85%, #eee); }
  .tile--white { background: linear-gradient(135deg, #f6f6f6, var(--white-stone) 50%, #d8d8d8 70%, #f4f4f4); }
  .tile--beige { background: linear-gradient(135deg, #e8d4bd, var(--beige-stone) 50%, #c9a887); }
  .tile--green { background: linear-gradient(135deg, #4fae6d, var(--green-stone) 55%, #2a7a47); }
  .tile--blue { background: linear-gradient(135deg, #5583b3, var(--blue-stone) 55%, #2d5078); }

  .page--one .tile { width: 80px; height: 81px; }
  .page--one .col-a { left: 238px; } .page--one .col-b { left: 325px; }
  .page--one .row-1 { top: 289px; } .page--one .row-2 { top: 375px; } .page--one .row-3 { top: 461px; }

  .page--two .section-tab { left: 182px; top: 0; width: 212px; height: 66px; }
  .page--two .section-tab-title { left: 28px; top: 35px; font-size: 14px; }
  .products-banner { left: 0; top: 68px; width: 181px; height: 128px;
    background: linear-gradient(90deg, var(--deep-green), var(--soft-green)); }
  .products-banner span { position: absolute; left: 26px; top: 40px; font-size: 27px; font-weight: 300; color: #d8ecc0; }
  .photo-carpet { left: 182px; top: 68px; width: 212px; height: 128px;
    background: radial-gradient(ellipse at 50% 45%, #cbb79c 0%, #a68c6c 45%, #5e4a36 80%, #3d2f22 100%); }
  .photo-hall { left: 0; top: 196px; width: 419px; height: 410px;
    background: linear-gradient(180deg, #ffffff 0%, #f6f3ec 30%, #ece4d0 60%, #d9ccaa 85%, #cdbb95 100%); }
  .text-column { left: 182px; top: 197px; width: 212px; height: 409px; background: var(--leaf-green); }
  .text-column-copy { position: absolute; left: 28px; top: 22px; width: 160px; font-size: 6.6px; line-height: 12.2px; color: #f4f9e6; }
  .text-column-copy p { margin-bottom: 4px; }
  .page--two .tile { width: 93px; height: 93px; }
  .page--two .col-a { left: 192px; } .page--two .col-b { left: 292px; }
  .page--two .row-1 { top: 404px; } .page--two .row-2 { top: 505px; }
</style>
</head>
<body>
<div class="board">
  <h1 class="board-title">Brochure page with using of multiple image</h1>

  <section class="page page--one">
    <div class="block section-tab"><span class="section-tab-title">Products</span></div>
    <div class="wordmark" style="left:318px;"><span class="wordmark-dot"></span>TLV8</div>
    <h2 class="block product-title">Marble</h2>
    <div class="block product-copy">
      <p>We all know the saying to seize the opportunity as it comes along because it only comes once.</p>
      <p>We believe in creating opportunities. With our diverse interests in portfolios, the company aims to provide its clients with the flexibility of choice to define their needs for services and acquire only the specific services. We promise to deliver quality services across several industries in setting up franchises or partnering services.</p>
      <p>The company has been formed by a group of people with significant knowledge and experience in Technology but also extending the company's horizon into Extreme Sports, Childcare and Food to name a few.</p>
      <p>We believe in making a difference. We value innovation, value and exceptional service for your investment, and empowering people who work with us.</p>
      <p>We always will bring the exceptional and quality services to you.</p>
    </div>
    <div class="block photo-lobby" role="img" aria-label="Photo of a marble-floored hotel lobby with palms and columns"></div>
    <div class="tile tile--orange col-a row-1" role="img" aria-label="Orange marble sample"></div>
    <div class="tile tile--grey-vein col-b row-1" role="img" aria-label="White marble with grey veins sample"></div>
    <div class="tile tile--white col-a row-2" role="img" aria-label="White marble sample"></div>
    <div class="tile tile--beige col-b row-2" role="img" aria-label="Beige marble sample"></div>
    <div class="tile tile--green col-a row-3" role="img" aria-label="Green marble sample"></div>
    <div class="tile tile--blue col-b row-3" role="img" aria-label="Blue marble sample"></div>
  </section>
  <p class="caption caption--one">Sapmle 01</p>

  <section class="page page--two">
    <div class="block photo-hall" role="img" aria-label="Photo of a bright hall with inlaid marble floor pattern"></div>
    <div class="wordmark" style="left:25px;"><span class="wordmark-dot"></span>TLV8</div>
    <div class="block section-tab"><span class="section-tab-title">Marble</span></div>
    <div class="block products-banner"><span>Products</span></div>
    <div class="block photo-carpet" role="img" aria-label="Photo of an inlaid marble floor medallion"></div>
    <div class="block text-column">
      <div class="text-column-copy">
        <p>Praesent iaculis dictum nunc sit amet dictum. Etiam ac velit ut sem accumsan venenatis vitae non diam. Suspendisse lobortis quam et dictum feugiat. Nulla ac convallis metus. In gravida dictum erat. Sed cursus feugiat ante feugiat commodo.</p>
        <p>Proin posuere rhoncus porttitor. Nulla blandit vulputate justo, sed sodales urna. Quisque posuere semper ligula a pellentesque. Vivamus egestas, orci eu dignissim posuere, nisl eros bibendum justo, in fringilla enim nibh rhoncus tellus. In euismod nulla ac nisl varius sodales a vitae dui. Vestibulum ac urna et.</p>
      </div>
    </div>
    <div class="tile tile--orange col-a row-1" role="img" aria-label="Orange marble sample"></div>
    <div class="tile tile--grey-vein col-b row-1" role="img" aria-label="White marble with grey veins sample"></div>
    <div class="tile tile--white col-a row-2" role="img" aria-label="White marble sample"></div>
    <div class="tile tile--beige col-b row-2" role="img" aria-label="Beige marble sample"></div>
  </section>
  <p class="caption caption--two">Sapmle 02</p>
</div>
</body>
</html>
```